Bref créative
Quorel Stationary
Stationary and Business Cards
I need double sided standard sized Business Card [3.5" x 2"]
show me your ideas
Corporate
Marcus Toddin
Chief Executive Officer
Halvenor Business Tower
18th Floor
PO Box 58217
Dubai
United Arab Emirates
mt@quorel.co
www.quorel.co
Show me your ideas

```html
<!DOCTYPE html>
<html lang="en">
<head>
<meta charset="utf-8">
<title>Quorel Stationary – Corporate Identity</title>
<link rel="stylesheet" href="https://fonts.googleapis.com/css2?family=Cinzel:wght@400;600&family=Open+Sans:wght@400;600&display=swap">
<style>
  :root{
    --bg:#ecebe8;
    --paper:#ffffff;
    --blue:#1b9ee0;
    --blue-deep:#0b6fb8;
    --blue-light:#7fd0f5;
    --ink:#4a4f55;
    --ink-soft:#8a9096;
    --line:#c9ccd0;
    --caption:#6b6e72;
  }
  *{box-sizing:border-box;margin:0;padding:0}
  html,body{width:1200px;height:932px;overflow:hidden;background:var(--bg)}
  body{position:relative;font-family:"Cinzel",serif;color:var(--ink)}

  .caption{position:absolute;font-family:"Open Sans",sans-serif;font-weight:600;font-size:11px;letter-spacing:.12em;color:var(--caption)}

  .piece{position:absolute;background:var(--paper);overflow:hidden;box-shadow:0 2px 8px rgba(0,0,0,.12)}
  .piece .swoosh{position:absolute;left:0;bottom:0;width:100%}

  .brand{position:absolute;display:flex;align-items:center;gap:8px}
  .brand-dot{flex:none;border-radius:50%;background:var(--blue)}
  .brand-name{font-family:"Cinzel",serif;font-weight:600;color:var(--blue-deep);white-space:nowrap}

  .address{position:absolute;font-size:7.5px;line-height:1.45;color:var(--ink);letter-spacing:.03em;white-space:nowrap}
  .address .email{display:flex;align-items:center;gap:5px;margin-top:3px}
  .address .email::before{content:"";width:9px;height:5px;background:var(--blue)}

  .web{position:absolute;font-size:9px;letter-spacing:.08em;color:#fff}

  /* fax */
  .fax{left:40px;top:60px;width:330px;height:466px}
  .fax .brand{left:26px;top:28px}
  .fax .address{left:168px;top:32px}
  .fax-title{position:absolute;left:26px;top:150px;font-family:"Open Sans",sans-serif;font-weight:400;font-size:26px;letter-spacing:.02em;color:#222}
  .fax-fields{position:absolute;left:26px;top:205px;width:230px;font-family:"Open Sans",sans-serif;font-size:9px;color:#333}
  .fax-fields li{list-style:none;display:flex;gap:6px;height:22px;align-items:flex-end}
  .fax-fields li span{flex:1;border-bottom:1px dotted #888;margin-bottom:2px}
  .fax-checks{position:absolute;left:26px;top:318px;display:flex;gap:30px;font-family:"Open Sans",sans-serif;font-size:9px;color:#333}
  .fax-checks span{display:flex;align-items:center;gap:5px}
  .fax-checks span::before{content:"";width:8px;height:8px;border:1px solid #999;background:#f3f3f3}
  .fax .web{right:22px;bottom:14px}

  /* letterhead */
  .letterhead{left:400px;top:60px;width:330px;height:466px}
  .letterhead .brand{left:26px;top:28px}
  .letterhead .address{left:168px;top:32px}
  .letterhead .web{right:22px;bottom:14px}

  /* envelope */
  .envelope{left:40px;top:580px;width:640px;height:320px}
  .envelope .brand{left:34px;top:30px}
  .envelope .address{left:34px;top:88px;font-size:8.5px}
  .envelope .web{right:28px;bottom:16px;font-size:10px}

  /* business cards */
  .card{width:390px;height:223px}
  .card-front{left:770px;top:60px}
  .card-back{left:770px;top:330px;background:linear-gradient(135deg,#f4f5f6,#cfd3d7)}
  .card-alt{left:770px;top:600px}
  .card .brand{left:22px;top:24px}
  .card-back .brand{left:50%;top:50%;transform:translate(-50%,-50%)}
  .person{position:absolute;left:170px;top:30px}
  .person-name{font-size:17px;color:var(--blue-deep);letter-spacing:.04em;white-space:nowrap}
  .person-title{font-size:8px;color:var(--ink-soft);letter-spacing:.06em;margin-top:2px}
  .card .address{left:170px;top:88px}
  .card .web{right:18px;bottom:10px}
  .card-alt .person{left:150px;top:26px}
  .card-alt .address{left:150px;top:84px}
</style>
</head>
<body>

<span class="caption" style="left:40px;top:40px">FAX</span>
<span class="caption" style="left:400px;top:40px">LETTERHEAD</span>
<span class="caption" style="left:770px;top:40px">BUSINESS CARD - FRONT</span>
<span class="caption" style="left:770px;top:310px">BUSINESS CARD - BACK</span>
<span class="caption" style="left:40px;top:560px">ENVELOPE</span>

<svg width="0" height="0" style="position:absolute" aria-hidden="true">
  <defs>
    <linearGradient id="sweep" x1="0" y1="0" x2="1" y2="0">
      <stop offset="0" stop-color="#7fd0f5"/>
      <stop offset=".45" stop-color="#1b9ee0"/>
      <stop offset="1" stop-color="#0b6fb8"/>
    </linearGradient>
  </defs>
</svg>

<!-- Fax -->
<section class="piece fax">
  <div class="brand"><span class="brand-dot" style="width:30px;height:30px"></span><span class="brand-name" style="font-size:16px">Quorel</span></div>
  <div class="address">
    Halvenor Business Tower<br>18th Floor, PO Box 58217<br>Dubai, United Arab Emirates
    <div class="email">mt@quorel.co</div>
  </div>
  <h1 class="fax-title">FAX</h1>
  <ul class="fax-fields">
    <li>To :<span></span></li>
    <li>Fax :<span></span></li>
    <li>Phone :<span></span></li>
    <li>Re :<span></span></li>
  </ul>
  <div class="fax-checks"><span>Urgent</span><span>For Review</span></div>
  <svg class="swoosh" viewBox="0 0 330 90" height="90" preserveAspectRatio="none" aria-hidden="true">
    <path d="M0,90 C120,86 240,60 330,0 L330,90 Z" fill="url(#sweep)"/>
    <path d="M0,84 C130,80 240,52 330,-6" fill="none" stroke="var(--line)" stroke-width="1.5"/>
  </svg>
  <span class="web">www.quorel.co</span>
</section>

<!-- Letterhead -->
<section class="piece letterhead">
  <div class="brand"><span class="brand-dot" style="width:30px;height:30px"></span><span class="brand-name" style="font-size:16px">Quorel</span></div>
  <div class="address">
    Halvenor Business Tower<br>18th Floor, PO Box 58217<br>Dubai, United Arab Emirates
    <div class="email">mt@quorel.co</div>
  </div>
  <svg class="swoosh" viewBox="0 0 330 90" height="90" preserveAspectRatio="none" aria-hidden="true">
    <path d="M0,90 C120,86 240,60 330,0 L330,90 Z" fill="url(#sweep)"/>
    <path d="M0,84 C130,80 240,52 330,-6" fill="none" stroke="var(--line)" stroke-width="1.5"/>
  </svg>
  <span class="web">www.quorel.co</span>
</section>

<!-- Envelope -->
<section class="piece envelope">
  <div class="brand"><span class="brand-dot" style="width:36px;height:36px"></span><span class="brand-name" style="font-size:19px">Quorel</span></div>
  <div class="address">
    Halvenor Business Tower, 18th Floor<br>PO Box 58217, Dubai, United Arab Emirates
  </div>
  <svg class="swoosh" viewBox="0 0 640 80" height="80" preserveAspectRatio="none" aria-hidden="true">
    <path d="M180,80 C380,78 540,55 640,0 L640,80 Z" fill="url(#sweep)"/>
    <path d="M170,76 C380,72 540,46 640,-6" fill="none" stroke="var(--line)" stroke-width="1.5"/>
  </svg>
  <span class="web">www.quorel.co</span>
</section>

<!-- Business card front -->
<section class="piece card card-front">
  <div class="brand"><span class="brand-dot" style="width:26px;height:26px"></span><span class="brand-name" style="font-size:15px">Quorel</span></div>
  <div class="person">
    <div class="person-name">Marcus Toddin</div>
    <div class="person-title">Chief Executive Officer</div>
  </div>
  <div class="address">
    Halvenor Business Tower, 18th Floor<br>PO Box 58217, Dubai<br>United Arab Emirates
    <div class="email">mt@quorel.co</div>
  </div>
  <svg class="swoosh" viewBox="0 0 390 60" height="60" preserveAspectRatio="none" aria-hidden="true">
    <path d="M0,60 C150,58 300,40 390,0 L390,60 Z" fill="url(#sweep)"/>
    <path d="M0,55 C160,52 300,32 390,-5" fill="none" stroke="var(--line)" stroke-width="1.2"/>
  </svg>
  <span class="web">www.quorel.co</span>
</section>

<!-- Business card back -->
<section class="piece card card-back">
  <div class="brand"><span class="brand-dot" style="width:40px;height:40px"></span><span class="brand-name" style="font-size:24px">Quorel</span></div>
</section>

<!-- Business card front, alternate -->
<section class="piece card card-alt">
  <svg class="swoosh" viewBox="0 0 390 223" height="223" preserveAspectRatio="none" aria-hidden="true" style="top:0">
    <path d="M0,0 L120,0 C100,80 70,170 0,223 Z" fill="url(#sweep)"/>
    <path d="M130,0 C110,80 80,170 8,223" fill="none" stroke="var(--line)" stroke-width="1.2"/>
  </svg>
  <div class="brand" style="left:14px;top:22px"><span class="brand-name" style="font-size:15px;color:#fff">Quorel</span></div>
  <div class="person">
    <div class="person-name">Marcus Toddin</div>
    <div class="person-title">Chief Executive Officer</div>
  </div>
  <div class="address">
    Halvenor Business Tower, 18th Floor<br>PO Box 58217, Dubai<br>United Arab Emirates
    <div class="email">mt@quorel.co</div>
  </div>
  <span class="web" style="color:var(--blue-deep)">www.quorel.co</span>
</section>

</body>
</html>
```